CSLN Banner

We need a design for a pull-up banner (850 x 2000 mm) to promote the Civic Strand Ledger Norm. https://cslnorm.net/en/
The banner action should be to get people to scan a QR code to join a mailing list (add a frame to add the QR code)

Use the website colours and typology https://cslnorm.net/en/
See also brochure for ideas https://cslnorm.net/documents/9/CSLN_brochure_english.pdf

```html
<!DOCTYPE html>
<html lang="en">
<head>
<meta charset="utf-8">
<title>CSLN Pull-up Banner</title>
<link rel="stylesheet" href="https://fonts.googleapis.com/css2?family=Montserrat:wght@400;500&family=Roboto:wght@700&display=swap">
<style>
  :root{
    --canvas:#e6e6e6;
    --ink:#0d0c1d;
    --map:#232323;
    --lime:#bfd02f;
    --blue:#3a8ccc;
    --white:#ffffff;
    --rule:#55556a;
    --body:#1e1e1e;
  }
  *{margin:0;padding:0;box-sizing:border-box}
  html,body{width:1200px;height:2199px;overflow:hidden;background:var(--canvas)}
  .canvas{position:relative;width:1200px;height:2199px;overflow:hidden;background:var(--canvas);font-family:"Montserrat",sans-serif}
  .brand-mark{position:absolute;left:0;width:100%;text-align:center;font-family:"Montserrat",sans-serif;font-weight:500;letter-spacing:-2px;line-height:1}
  .brand-mark--display{top:92px;font-size:170px;color:var(--ink)}
  .banner{position:absolute;left:215px;top:387px;width:770px;height:1812px;background:var(--white);overflow:hidden}
  .banner-hero{position:absolute;left:0;top:0;width:770px;height:850px;background:var(--ink);clip-path:polygon(0 0,100% 0,100% 349px,0 501px)}
  .brand-mark--banner{top:40px;font-size:96px;color:var(--white)}
  .headline{position:absolute;left:67px;top:178px;font-family:"Roboto",sans-serif;font-weight:700;font-size:50px;line-height:57px;color:var(--white)}
  .headline-rule{position:absolute;left:67px;top:302px;width:435px;height:2px;background:var(--rule)}
  .tagline{position:absolute;left:67px;top:318px;font-size:22px;line-height:26px;color:var(--white)}
  .hero-map{position:absolute;left:0;top:0;width:770px;height:860px;background:linear-gradient(100deg,#262626,#1f1f1f 60%,#2a2a2a);clip-path:polygon(0 501px,100% 349px,100% 696px,0 851px)}
  .accent-stripe{position:absolute;left:0;top:0;width:770px;height:860px;background:var(--lime);clip-path:polygon(236px 820px,100% 696px,100% 714px,236px 836px)}
  .section{position:absolute;left:70px;width:640px}
  .section-title{font-family:"Roboto",sans-serif;font-weight:700;font-size:25px;line-height:30px;color:var(--blue)}
  .section-title--large{font-size:31px;line-height:36px}
  .section-text{font-size:19.5px;line-height:29px;color:var(--body);margin-top:6px}
  .benefits{position:absolute;left:70px;top:1213px;width:660px;display:grid;grid-template-columns:354px 300px;row-gap:16px}
  .benefit{display:flex;gap:12px;font-size:19.5px;line-height:29px;color:var(--body)}
  .benefit svg{flex:0 0 34px;width:34px;height:34px;margin-top:2px}
  .benefit strong{font-weight:500;color:var(--ink)}
  .footer-band{position:absolute;left:0;top:1462px;width:770px;height:14px;background:var(--lime)}
  .footer{position:absolute;left:0;top:1476px;width:770px;height:336px;background:var(--ink)}
  .community-icon{position:absolute;left:50px;top:40px;width:84px;height:84px}
  .cta-title{position:absolute;left:52px;top:137px;font-family:"Roboto",sans-serif;font-weight:700;font-size:33px;line-height:40px;color:var(--lime)}
  .cta-text{position:absolute;left:52px;top:180px;font-size:19px;line-height:29px;color:var(--lime)}
  .contacts{position:absolute;left:52px;top:248px;display:flex;gap:14px;align-items:center;font-size:19px;color:var(--white)}
  .contacts span{display:flex;align-items:center;gap:8px}
  .contacts .email{color:var(--lime)}
  .qr-frame{position:absolute;left:510px;top:64px;width:208px;height:206px;background:var(--white);border-radius:12px}
</style>
</head>
<body>
<div class="canvas">
  <div class="brand-mark brand-mark--display">csln</div>

  <section class="banner">
    <div class="banner-hero">
      <div class="brand-mark brand-mark--banner">csln</div>
      <h1 class="headline">Mapping the world's<br>Internet backbone.</h1>
      <div class="headline-rule"></div>
      <p class="tagline">A community-driven standard for mapping<br>and sharing fibre network data.</p>
    </div>
    <div class="hero-map" role="img" aria-label="Dark world map with coloured fibre network routes across Africa, Brazil and Central America"></div>
    <div class="accent-stripe"></div>

    <div class="section" style="top:897px">
      <h2 class="section-title">The Problem</h2>
      <p class="section-text">Lack of reliable fibre data leads to gaps, duplication, and poor infrastructure planning.</p>
    </div>
    <div class="section" style="top:1010px">
      <h2 class="section-title">The Solution</h2>
      <p class="section-text">CSLN provides a common language to exchange, analyze,<br>and visualize fibre network data — improving transparency and decision-making.</p>
    </div>
    <div class="section" style="top:1158px">
      <h2 class="section-title section-title--large">Who Benefits</h2>
    </div>

    <div class="benefits">
      <div class="benefit">
        <svg viewBox="0 0 34 34" aria-hidden="true"><path fill="#1e1e1e" d="M17 2 1 9v3h32V9z M4 14h4v12H4z M11 14h4v12h-4z M19 14h4v12h-4z M26 14h4v12h-4z M1 28h32v4H1z"/></svg>
        <div><strong>Governments &amp; regulators</strong> identify network gaps and weaknesses</div>
      </div>
      <div class="benefit">
        <svg viewBox="0 0 34 34" aria-hidden="true"><rect x="9" y="2" width="20" height="25" rx="3" fill="#1e1e1e"/><rect x="4" y="7" width="20" height="25" rx="3" fill="#fff" stroke="#1e1e1e" stroke-width="2.5"/><path d="M9 14h10M9 19h10M9 24h10" stroke="#1e1e1e" stroke-width="2.5"/></svg>
        <div><strong>Avoid duplication</strong> in fibre infrastructure reporting</div>
      </div>
      <div class="benefit">
        <svg viewBox="0 0 34 34" aria-hidden="true"><rect x="10" y="1" width="14" height="15" rx="3" fill="#1e1e1e"/><path d="M17 4v10M20 6h-5a1.5 1.5 0 0 0 0 3h4a1.5 1.5 0 0 1 0 3h-5" stroke="#fff" stroke-width="1.6" fill="none"/><path d="M3 33v-7a8 8 0 0 1 8-8h12a8 8 0 0 1 8 8v7z" fill="#1e1e1e"/><path d="M17 19v13" stroke="#fff" stroke-width="2"/></svg>
        <div><strong>Investors &amp; planners</strong> make data-driven decisions</div>
      </div>
      <div class="benefit">
        <svg viewBox="0 0 34 34" aria-hidden="true"><path d="M5 9a8 6 0 0 1 16 0z M3 9h20v2H3z" fill="#1e1e1e"/><path d="M2 33v-8a7 7 0 0 1 7-7h8a7 7 0 0 1 7 7v8z" fill="#1e1e1e"/><circle cx="28" cy="20" r="4" fill="#1e1e1e"/><path d="M28 24v9" stroke="#1e1e1e" stroke-width="2.5"/></svg>
        <div><strong>Engineers &amp; researchers</strong> access standardized GIS-ready data</div>
      </div>
    </div>

    <div class="footer-band"></div>
    <div class="footer">
      <svg class="community-icon" viewBox="0 0 84 84" aria-hidden="true">
        <circle cx="42" cy="42" r="36" fill="none" stroke="#bfd02f" stroke-width="2.5"/>
        <circle cx="42" cy="6" r="5" fill="#0d0c1d" stroke="#bfd02f" stroke-width="2.5"/>
        <circle cx="10" cy="60" r="5" fill="#0d0c1d" stroke="#bfd02f" stroke-width="2.5"/>
        <circle cx="74" cy="60" r="5" fill="#0d0c1d" stroke="#bfd02f" stroke-width="2.5"/>
        <circle cx="42" cy="35" r="6" fill="#bfd02f"/>
        <circle cx="28" cy="39" r="5" fill="#bfd02f"/>
        <circle cx="56" cy="39" r="5" fill="#bfd02f"/>
        <path d="M31 56a11 11 0 0 1 22 0z M18 55a10 9 0 0 1 14-7v7z M66 55a10 9 0 0 0-14-7v7z" fill="#bfd02f"/>
      </svg>
      <h2 class="cta-title">Join the CSLN Mailing List</h2>
      <p class="cta-text">To stay up to date with and contribute to the<br>development and adoption of CSLN.</p>
      <div class="contacts">
        <span><svg width="14" height="14" viewBox="0 0 14 14" aria-hidden="true"><circle cx="7" cy="7" r="6" fill="#fff"/><path d="M4 4c2 1 3 0 4 2s-2 3-1 6M9 2c0 2 2 2 3 4" stroke="#0d0c1d" stroke-width="1.3" fill="none"/></svg>www.cslnorm.net</span>
        <span class="email"><svg width="17" height="13" viewBox="0 0 17 13" aria-hidden="true"><rect width="17" height="13" rx="2" fill="#bfd02f"/><path d="M1 2l7.5 5L16 2" stroke="#0d0c1d" stroke-width="1.5" fill="none"/></svg>outreach@cslnorm.net</span>
      </div>
      <div class="qr-frame" aria-label="QR code frame"></div>
    </div>
  </section>
</div>
</body>
</html>
```